Tor Ridge Wine Club-The Onyx Roll

We are a new aspirational brand of fine Tasmania Wine. We need a commitment club poster which appeals to the ego.We have one opportunity to get customers to sign up and that is when they visit at the cellar door. This club is the core of our business.

The brand is a clean, pure , simple brand, black and white very sophiscated.
This is a top end product.

Our Commitment Club is named The Onyx Roll which is a play on words. Tradionally The Onyx Roll is a list of people that you dont want to do business with. So we are turning this on its had.

You need to make this poster sharp, desirable, possibly sexy but masculine. Im thinking Felix Crane . It doesnt matter the client will be 40 up fashion consious looking for something new , exclusive , something there peers don't have.

I dont like busy! make it clean clear and basically undeniable. The client must not be able to resist the offer.

www.torridgevines.com.au

Reason: Internet problems so cant get to respond and offer comment in a timely manner

Appreciator 40-60 male wants to be recognised fashion consious sophiscated has money and wants to part of something exclusive.

A feeling that you are part of something that only a few are. Exclusive

Maybe an imagine of beautiful people 30/40ish I want to be drinking Tor Wine / in The Onyx Roll

Fashion

Must have
• Tor Ridge Logo
TOR Bottles images

We produce only 1600 cases of wine each vintage. Therefore we have limited membership 001-999 for our club.
Award Winning Wines available exclusively from us.

Gold Member
We will reserve 2 cases of our limited vintage, to be delivered to you in May and Oct.
Single varietal or mixed cases. You receive a 15% discount.

Silver Member
We will reserve 1 case of our limited vintage to be delivered to you 6 bottles in May and 6 in Oct.
Single varietal or mixed cases. You receive a 10% discount.

To you exclusively from us not, available from any other retailers.

You will be invited to Onyx Roll Only Events and Tastings.
You will get preferential access to new and limited releases.
Members will be entered in a bi annual draw to win a 2 night stay here at the Tor Weavers Cottage on the Freycinet Coast Tasmania.

• VIP stamps,gimacs, anything that cheapens our brand.

We do not like busy posters please have white space

```html
<!DOCTYPE html>
<html lang="en">
<head>
<meta charset="utf-8">
<title>Tor Ridge – Join the Onyx Roll</title>
<link href="https://fonts.googleapis.com/css2?family=Great+Vibes&family=Cinzel:wght@400&family=Cormorant+SC:wght@400;500&display=swap" rel="stylesheet">
<style>
  :root {
    --bg-deep: #050505;
    --bg-stripe: #141414;
    --ink-white: #f4f4f2;
    --ink-gold: #c9a24a;
    --ink-gold-soft: #b08a3c;
    --ink-silver: #d9d9d9;
    --ink-grey: #8a8a8a;
    --tie-light: #6a6a6a;
    --tie-dark: #0d0d0d;
  }
  * { margin: 0; padding: 0; box-sizing: border-box; }
  html, body { width: 724px; height: 1200px; overflow: hidden; background: var(--bg-deep); }
  .poster {
    position: relative;
    width: 724px; height: 1200px;
    background:
      repeating-linear-gradient(90deg, var(--bg-stripe) 0 1px, transparent 1px 6px),
      radial-gradient(ellipse at 50% 10%, #1e1e1e 0%, var(--bg-deep) 70%);
    color: var(--ink-white);
    text-align: center;
    font-family: "Cormorant SC", "Cinzel", serif;
  }
  .bow-tie {
    position: absolute; left: 150px; top: 18px; width: 424px; height: 230px;
    border-radius: 44% 44% 44% 44% / 50% 50% 50% 50%;
    background:
      radial-gradient(ellipse 16% 28% at 50% 50%, #9a9a9a 0%, #3a3a3a 70%, transparent 100%),
      radial-gradient(ellipse at 30% 40%, var(--tie-light) 0%, #2a2a2a 45%, var(--tie-dark) 80%),
      var(--tie-dark);
    opacity: .95;
  }
  .brand {
    position: absolute; top: 268px; left: 0; width: 100%;
    font-family: "Great Vibes", cursive;
    font-size: 92px; line-height: 1; color: var(--ink-white);
  }
  .invite { position: absolute; top: 384px; left: 0; width: 100%; font-size: 17px; letter-spacing: 1px; }
  .headline {
    position: absolute; top: 410px; left: 0; width: 100%;
    font-family: "Great Vibes", cursive; font-size: 50px; color: var(--ink-gold);
  }
  .divider {
    position: absolute; left: 322px; width: 80px; height: 14px;
    background: linear-gradient(90deg, transparent, var(--ink-gold-soft) 30%, var(--ink-gold) 50%, var(--ink-gold-soft) 70%, transparent);
    border-radius: 7px; opacity: .85;
  }
  .divider--top { top: 474px; }
  .divider--bottom { top: 985px; }
  .levels { position: absolute; top: 508px; left: 0; width: 100%; font-family: "Cinzel", serif; font-size: 23px; letter-spacing: 2px; }
  .tier { position: absolute; left: 0; width: 100%; }
  .tier--gold { top: 575px; color: var(--ink-gold); }
  .tier--silver { top: 760px; color: var(--ink-silver); }
  .tier__name { font-family: "Great Vibes", cursive; font-size: 62px; line-height: 1.1; }
  .tier__terms { font-size: 22px; line-height: 27px; margin-top: 2px; letter-spacing: .5px; }
  .tier__terms .muted { color: var(--ink-grey); }
  .tier--gold .tier__terms { color: var(--ink-gold); }
  .perks {
    position: absolute; top: 1040px; left: 0; width: 100%;
    font-size: 13.5px; line-height: 17px; letter-spacing: .4px; color: var(--ink-white);
  }
  .perks p + p { margin-top: 0; }
  .perks .lead { margin-bottom: 14px; }
</style>
</head>
<body>
<main class="poster">
  <div class="bow-tie" role="img" aria-label="Black satin bow tie"></div>

  <h1 class="brand">Tor Ridge</h1>
  <p class="invite">invites you to</p>
  <h2 class="headline">Join the Onyx Roll</h2>
  <div class="divider divider--top" role="img" aria-label="Small gold flourish"></div>

  <p class="levels">Two levels of commitment</p>

  <section class="tier tier--gold">
    <h3 class="tier__name">Gold Membership</h3>
    <p class="tier__terms">We will reserve 2 cases of our limited vintage, to<br>be delivered to you in May and Oct.<br>Single varietal or mixed cases. You receive a 15% discount.</p>
  </section>

  <section class="tier tier--silver">
    <h3 class="tier__name">Silver Membership</h3>
    <p class="tier__terms">We will reserve 1 case of our limited vintage to be<br><span class="muted">delivered to you 6 bottles in May and 6 in Oct.</span><br>Single varietal or mixed cases. You receive a 10% discount.</p>
  </section>

  <div class="divider divider--bottom" role="img" aria-label="Small gold flourish"></div>

  <section class="perks">
    <p class="lead">To you exclusively from us not, available from any other retailers.</p>
    <p>You will be invited to Onyx Roll Only Events and Tastings.</p>
    <p>You will get preferential access to new and limited releases.</p>
    <p>Members will be entered in a bi annual draw to win a 2 night stay here at</p>
    <p>the Tor Weavers Cottage on the Freycinet Coast Tasmania.</p>
  </section>
</main>
</body>
</html>
```